Create a premium soap bar box bar design for an all-natural, men's skincare brand.

We are launching a men’s premium, natural soap bar and skincare business. To start, we will be launching cold-press, all-natural soap bars with a few additional products such as lotions. We plan to expand our line into additional skincare products such as face exfoliants, moisturizers and cleansers that target basic needs such as anti-aging, clarifying and hydrating.

Our target audience is men ages 25-50, with a secondary audience of male teens. Our target audience are mid to high income, professionals that live in more urban areas, but enjoy being active outdoors after work and on the weekends. Our target audience are hard workers, humble and want to enjoy all that life has to offer – whether that’s on top of a mountain or an ocean wave. They hike, bike, skateboard, surf or any other sport that gets them outside. They are husbands, brothers and fathers – there for their family and friends.

Our brand is sophisticated, adventurous and has a sense of humor. Many of our competitors either focus on the rugged outdoors or are more pretentious. We are in-between. We are free spirited and love the fresh air. Our products are trustworthy with no toxic chemicals or harsh ingredients. We are all-natural and provide high-quality, premium products that our audience expects and deserves.

Target Market(s)

Men, ages 25-54 who are high-earning professionals, yet enjoy getting outdoors and being active on the weekends - hiking, biking, surfing, skateboarding and more.

Industry/Entity Type

Men's skincare

Font styles to use
Sans Serif

Requirements
Must have
• See attachments
Nice to have
• We would prefer to a have a premium, slightly more modern looking design that will appeal to our target audience and slightly higher price point.
Should not have
• Please do not include an icon for the fragrance, i.e. cinnamon sticks. However, we do need some differentiation for the fragrance, i.e. color, etc. as it will be on the shelf with other fragrances.

```html
<!DOCTYPE html>
<html lang="en">
<head>
<meta charset="utf-8">
<title>Ridge Hale – Men's Natural Soap Box Dieline</title>
<link href="https://fonts.googleapis.com/css2?family=Montserrat:wght@400;500;600;700&display=swap" rel="stylesheet">
<style>
  :root {
    --navy: #0f2847;
    --kraft: #d2b096;
    --red: #e8463f;
    --white: #ffffff;
    --page: #ffffff;
  }
  html, body {
    margin: 0;
    width: 1200px;
    height: 651px;
    overflow: hidden;
    background: var(--page);
  }
  .canvas {
    position: relative;
    width: 1200px;
    height: 651px;
  }
  .dieline {
    position: absolute;
    left: 386px;
    top: 15px;
    width: 427px;
    height: 620px;
    font-family: 'Montserrat', sans-serif;
  }
  .kraft { fill: var(--kraft); }
  .navy { fill: var(--navy); }
  .brand-name { font-weight: 600; }
  .tagline { font-weight: 500; }
  .body-copy { font-weight: 600; letter-spacing: 1px; }
  .ingredients { font-weight: 400; }
</style>
</head>
<body>
<main class="canvas">
  <svg class="dieline" viewBox="30 22 656 953" xmlns="http://www.w3.org/2000/svg">
    <!-- Box structure -->
    <g class="box-structure">
      <rect class="kraft" x="162" y="22" width="393" height="953"/>
      <rect class="kraft side-flap-left" x="30" y="153" width="132" height="346"/>
      <rect class="kraft side-flap-right" x="555" y="153" width="131" height="346"/>
      <rect class="navy front-panel" x="207" y="22" width="295" height="438"/>
      <rect class="navy back-panel" x="207" y="499" width="295" height="476"/>
      <line class="back-divider" x1="207" y1="630" x2="502" y2="630" stroke="#2c4566" stroke-width="1"/>
    </g>

    <!-- Top tuck flap (reads upside down) -->
    <g class="top-flap" transform="rotate(180 355 60)">
      <text x="355" y="78" text-anchor="middle" class="brand-name" font-size="20" fill="var(--white)" letter-spacing="1">RIDGE HALE</text>
      <text x="355" y="91" text-anchor="middle" class="tagline" font-size="6" fill="var(--white)" letter-spacing="4">REAL SKINCARE</text>
    </g>
    <circle class="brand-dot" cx="355" cy="110" r="27" fill="none" stroke="var(--white)" stroke-width="3"/>

    <!-- Front panel -->
    <g class="front-panel-content">
      <text x="357" y="188" text-anchor="middle" font-size="16" font-weight="500" fill="var(--kraft)" letter-spacing="3">MEN'S NATURAL SOAP</text>
      <circle class="brand-dot" cx="350" cy="314" r="45" fill="none" stroke="var(--white)" stroke-width="4"/>
      <text x="350" y="405" text-anchor="middle" class="brand-name" font-size="36" fill="var(--white)" letter-spacing="1">RIDGE HALE</text>
      <text x="350" y="424" text-anchor="middle" class="tagline" font-size="11" fill="var(--white)" letter-spacing="5">REAL SKINCARE</text>
    </g>

    <!-- Fragrance strip -->
    <g class="fragrance-strip">
      <text x="207" y="479" font-size="17" font-weight="700" fill="var(--navy)">CINNAMON BARK</text>
      <text x="492" y="478" text-anchor="end" font-size="12" font-weight="500" fill="var(--navy)">5 Oz. Bar</text>
    </g>

    <!-- Left side flap -->
    <g class="side-flap-left-content">
      <circle cx="112" cy="208" r="29" fill="none" stroke="var(--navy)" stroke-width="3"/>
      <text transform="translate(107 250) rotate(90)" class="brand-name" font-size="32" fill="var(--navy)">RIDGE HALE</text>
      <text transform="translate(89 250) rotate(90)" class="tagline" font-size="9" fill="var(--red)" letter-spacing="5">REAL SKINCARE</text>
      <text transform="translate(47 185) rotate(90)" font-size="12" fill="var(--navy)"><tspan font-weight="700">Directions:</tspan> Lather, rinse and repeat.</text>
    </g>

    <!-- Right side flap -->
    <g class="side-flap-right-content">
      <circle cx="602" cy="450" r="29" fill="none" stroke="var(--navy)" stroke-width="3"/>
      <text transform="translate(609 410) rotate(-90)" class="brand-name" font-size="32" fill="var(--navy)">RIDGE HALE</text>
      <text transform="translate(625 410) rotate(-90)" class="tagline" font-size="9" fill="var(--red)" letter-spacing="5">REAL SKINCARE</text>
      <text transform="translate(657 476) rotate(-90)" font-size="12" font-weight="500" fill="var(--navy)">Check out all our products at ridgehale.com</text>
    </g>

    <!-- Back panel: distributor -->
    <g class="distributor">
      <text x="222" y="522" font-size="13" fill="var(--white)">Distributed by:</text>
      <text x="222" y="546" font-size="13" fill="var(--white)">Northpine Goods Duluth, MN 55802</text>
      <g class="recycle-icon" fill="none" stroke="var(--kraft)" stroke-width="5" stroke-linejoin="round">
        <path d="M251 566 L271 598 L231 598 Z"/>
        <path d="M265 576 l7 -2 l0 8" stroke-width="3"/>
      </g>
    </g>

    <!-- Back panel: copy, ingredients and badges (upside down) -->
    <g class="back-copy" transform="rotate(180 354.5 802)">
      <g class="body-copy" font-size="9.5" fill="var(--white)">
        <text x="229" y="658" textLength="258" lengthAdjust="spacing">REAL INGREDIENTS FOR REAL GUYS.</text>
        <text x="229" y="680" textLength="258" lengthAdjust="spacing">BRING THE OUTDOORS IN USING REAL,</text>
        <text x="229" y="702" textLength="258" lengthAdjust="spacing">NATURAL INGREDIENTS ON YOUR SKIN.</text>
        <text x="229" y="724" textLength="258" lengthAdjust="spacing">TRADITIONAL BAR SOAP CONTAINS HARSH</text>
        <text x="229" y="746" textLength="258" lengthAdjust="spacing">CHEMICAL INGREDIENTS THAT CAN BE</text>
        <text x="229" y="768" textLength="258" lengthAdjust="spacing">HARMFUL TO YOU AND THE ENVIRONMENT.</text>
        <text x="229" y="790" textLength="258" lengthAdjust="spacing">LATHER UP WITH RIDGE HALE'S HANDCRAFTED,</text>
        <text x="229" y="812" textLength="258" lengthAdjust="spacing">ALL-NATURAL SOAP AND FEEL THE DIFFERENCE</text>
      </g>
      <g class="ingredients" font-size="9" fill="var(--white)">
        <text x="229" y="840" textLength="258" lengthAdjust="spacing"><tspan font-weight="700">Ingredients:</tspan> Vegetable Oil Blend (Olive Oil, Organic</text>
        <text x="229" y="857" textLength="258" lengthAdjust="spacing">Sustainable Palm Oil, Coconut Oil, Shea Butter,</text>
        <text x="229" y="874" textLength="258" lengthAdjust="spacing">Sunflower Oil), Water, Sodium Hydroxide, Beeswax,</text>
        <text x="229" y="891">Cinnamon Essential Oil, Honey, Ground Cinnamon.</text>
      </g>
      <g class="badges">
        <circle cx="347" cy="936" r="19" fill="var(--kraft)"/>
        <circle cx="404" cy="936" r="19" fill="var(--kraft)"/>
        <circle cx="461" cy="936" r="19" fill="var(--kraft)"/>
        <rect x="237" y="920" width="72" height="26" fill="var(--red)" role="img" aria-label="Waving flag illustration"/>
        <text x="273" y="961" text-anchor="middle" font-size="8" fill="var(--white)">Made in the USA</text>
      </g>
    </g>
  </svg>
</main>
</body>
</html>
```